Wordpress design for company website

We need a Wordpress design for a new brand of payment service called 705. Please see 2 mockup pages attached as guidance.

Reason: Hi all, we're extending the deadline for this design project by 7 days to have more time for more design submissions to come in.

Thank you.

Target Market(s)

Consumers in Southeast Asia with no credit cards

Industry/Entity Type

It Company

Requirements
Should not have
• Too much color

```html
<!DOCTYPE html>
<html lang="en">
<head>
<meta charset="utf-8">
<title>705 – Payment service for your business</title>
<link href="https://fonts.googleapis.com/css2?family=Arimo:wght@400;700&display=swap" rel="stylesheet">
<style>
:root{
  --text:#555a5f;
  --heading:#5e6368;
  --muted:#6d7277;
  --line:#d6d8da;
  --sky:#8fd0ef;
  --blue:#22a7e0;
  --navy:#1b5aa0;
  --green:#2f9e2f;
  --white:#ffffff;
  --card:#e4e6e8;
}
*{box-sizing:border-box;margin:0;padding:0}
html,body{width:1200px;height:1158px;overflow:hidden;background:var(--white)}
body{position:relative;font-family:"Arimo",Arial,sans-serif;color:var(--text)}
a{color:inherit;text-decoration:none}
.abs{position:absolute}

.top-links{left:880px;top:18px;width:228px;text-align:right;font-size:15px;font-weight:700;color:var(--muted)}
.top-links span{margin:0 6px}
.brand{left:90px;top:60px;display:flex;align-items:center;gap:10px;font-size:52px;font-weight:700;color:var(--green)}
.brand i{display:block;width:22px;height:22px;border-radius:50%;background:var(--green)}

.btn{display:flex;align-items:center;justify-content:center;font-size:15px;font-weight:700;color:var(--white);box-shadow:0 2px 4px rgba(0,0,0,.18)}
.btn-sky{background:var(--sky)}
.btn-blue{background:var(--blue)}
.btn-navy{background:var(--navy)}
.nav-what{left:712px;top:62px;width:177px;height:57px}
.nav-biz{left:913px;top:62px;width:195px;height:57px}
.nav-faq{left:1131px;top:62px;width:58px;height:57px}

.side-tab{left:1146px;top:219px;width:42px;height:109px;background:var(--navy);border:3px solid var(--white);box-shadow:0 1px 4px rgba(0,0,0,.3);display:flex;align-items:center;justify-content:center}
.side-tab span{transform:rotate(-90deg);color:var(--white);font-weight:700;font-size:15px;white-space:nowrap}

.hero{left:64px;top:150px;width:1044px;height:280px;border:1px solid var(--line);border-radius:8px}
.hero-title{left:122px;top:176px;width:440px;font-size:22px;line-height:26px;font-weight:700;color:var(--heading);letter-spacing:-.4px;white-space:nowrap}
.hero-copy{left:122px;top:212px;width:428px;font-size:15px;line-height:19px;color:var(--text)}
.hero-btn{left:118px;top:349px;width:177px;height:56px}
.hero-photo{left:589px;top:172px;width:493px;height:237px;border-radius:8px;background:linear-gradient(120deg,#c9d3d9 0%,#8e9aa2 35%,#5f6c75 55%,#b7c2c8 80%,#dfe5e8 100%);box-shadow:0 2px 6px rgba(0,0,0,.25)}

.card{top:466px;height:183px;border-radius:3px;overflow:hidden;background:var(--card)}
.card-1{left:64px;width:309px;background:linear-gradient(135deg,#f3dcd7,#ecc9c4 40%,#e9e4ea 80%)}
.card-2{left:430px;width:312px;background:linear-gradient(90deg,#5fc44e 0%,#8dd66e 35%,#dfe2e3 55%,#e2e4e5 100%)}
.card-3{left:797px;width:311px;background:linear-gradient(90deg,#c8ccd0 0%,#e6e8ea 50%,#e8eaeb 100%)}
.card-label{top:478px;height:35px;background:rgba(255,255,255,.9);font-size:20px;font-weight:700;color:var(--muted);display:flex;align-items:center;padding-left:24px;box-shadow:0 1px 3px rgba(0,0,0,.12)}
.slider{left:94px;top:527px;width:250px;height:53px;background:#b9bcc0;display:flex;align-items:center;justify-content:space-between;padding:0 3px}
.slider-arrow{width:10px;height:47px;background:#d5d7d9;display:flex;align-items:center;justify-content:center}
.slider-face{width:218px;height:47px;background:var(--white);display:flex;align-items:center;justify-content:center;font-size:30px;font-weight:700;color:var(--navy)}
.card-btn{top:596px;height:38px;font-size:16px}
.stat{left:560px;top:510px;width:165px;text-align:right;color:var(--muted);font-weight:700;font-size:15px;line-height:19px}
.stat strong{display:block;font-size:30px;line-height:34px;color:var(--muted)}
.mini-brand{left:1012px;top:480px;font-size:26px;font-weight:700;color:var(--green)}
.pitch{left:912px;top:526px;width:180px;text-align:right;font-size:14px;font-weight:700;line-height:19px;color:var(--muted)}
.pitch-art{left:797px;top:510px;width:110px;height:139px;background:linear-gradient(160deg,#59c149,#2f9e2f 60%,#bfc4c8)}

.col h2{font-size:19px;font-weight:700;color:var(--heading);margin-bottom:6px}
.col p{font-size:15px;line-height:19px;text-align:justify}
.col-left{left:64px;top:690px;width:502px}
.col-right{left:611px;top:690px;width:490px}
.more{top:826px;font-size:15px;font-weight:700;color:var(--blue);border-bottom:1px solid var(--blue);padding-bottom:1px}

.footer{left:64px;top:881px;width:1044px;height:194px;border:1px solid var(--line);border-radius:8px}
.f-head{font-size:15px;font-weight:700;color:var(--muted)}
.f-list{font-size:11px;line-height:13px;color:var(--text);list-style:none}
.f-div{top:910px;width:1px;height:78px;background:var(--line)}
.f-link{font-size:13px;font-weight:700;color:var(--blue);border-bottom:1px solid var(--blue)}
.f-fan{font-size:13px;font-weight:700;color:var(--muted)}
.social{top:988px;width:25px;height:25px;border-radius:4px}
.legal{left:64px;top:1040px;width:1044px;text-align:center;font-size:11px;color:var(--text)}
.legal span{margin:0 5px}
.copyright{left:65px;top:1085px;width:1043px;height:30px;background:var(--blue);color:var(--white);font-size:11px;font-weight:700;display:flex;align-items:center;justify-content:center}
</style>
</head>
<body>

<div class="abs top-links"><a href="#">View my transactions</a><span>|</span><a href="#">Sign In</a></div>
<div class="abs brand"><i></i>705</div>

<a class="abs btn btn-sky nav-what" href="#">What is 705?</a>
<a class="abs btn btn-blue nav-biz" href="#">Use 705 for my Biz</a>
<a class="abs btn btn-navy nav-faq" href="#">FAQ</a>

<a class="abs side-tab" href="#"><span>Circlely</span></a>

<section class="abs hero"></section>
<h1 class="abs hero-title">How do I use 705 service with my business?</h1>
<p class="abs hero-copy">Lorem Ipsum is simply dummy text of the printing and typesetting industry. Lorem Ipsum has been the industry's standard dummy text ever since the 1500s, when an unknown printer took a galley of type and scrambled it to make a type specimen book. It has survived not only five centuries, but also the leap into electronic typesetting, remaining essentially</p>
<a class="abs btn btn-sky hero-btn" href="#">What is 705?</a>
<div class="abs hero-photo" role="img" aria-label="Photo of three colleagues working together at a laptop in an office"></div>

<div class="abs card card-1" role="img" aria-label="Soft pink swirl pattern background"></div>
<div class="abs card-label" style="left:60px;width:190px">705 Merchants</div>
<div class="abs slider">
  <span class="slider-arrow"><svg width="6" height="10" viewBox="0 0 6 10"><path d="M5 1 1 5l4 4" fill="none" stroke="#8a8e92" stroke-width="1.5"/></svg></span>
  <span class="slider-face">Circlely</span>
  <span class="slider-arrow"><svg width="6" height="10" viewBox="0 0 6 10"><path d="M1 1l4 4-4 4" fill="none" stroke="#8a8e92" stroke-width="1.5"/></svg></span>
</div>
<a class="abs btn btn-sky card-btn" href="#" style="left:230px;width:125px">Read More</a>

<div class="abs card card-2" role="img" aria-label="Green globe illustration showing the Americas"></div>
<div class="abs card-label" style="left:426px;width:186px">Locations</div>
<div class="abs stat">More than<strong>12000</strong>payment locations.</div>
<a class="abs btn btn-blue card-btn" href="#" style="left:548px;width:177px">Show Locations</a>

<div class="abs card card-3"></div>
<div class="abs pitch-art" role="img" aria-label="Illustration of a green figure with a briefcase striding ahead of a grey crowd"></div>
<div class="abs card-label" style="left:792px;width:187px">Sign Up</div>
<div class="abs mini-brand">705</div>
<div class="abs pitch">Are you interested in 705<br>as a payment option<br>for your business?</div>
<a class="abs btn btn-navy card-btn" href="#" style="left:910px;width:178px;font-size:15px">Become 705 Merchant</a>

<article class="abs col col-left">
  <h2>Show what makes 705 special</h2>
  <p>There are many variations of passages of Lorem Ipsum available, but the majority have suffered alteration in some form, by injected humour, or randomised words which don't look even slightly believable. If you are going to use a passage of Lorem Ipsum, you need to be sure there isn't anything embarrassing hidden in the middle of text.</p>
</article>
<a class="abs more" href="#" style="left:411px">Learn more about 705</a>

<article class="abs col col-right">
  <h2>How to integrate 705?</h2>
  <p>It is a long established fact that a reader will be distracted by the readable content of a page when looking at its layout. The point of using Lorem Ipsum is that it has a more-or-less normal distribution of letters, as opposed to using 'Content here, content here', making it look like readable English.</p>
</article>
<a class="abs more" href="#" style="left:867px">See many steps of 705 integration</a>

<footer class="abs footer"></footer>
<div class="abs f-head" style="left:132px;top:906px">Choose your Region</div>
<ul class="abs f-list" style="left:133px;top:938px"><li>Thailand</li><li>Pjilippine</li><li>Vietnam</li></ul>
<ul class="abs f-list" style="left:242px;top:938px"><li>Malaysia</li><li>Singapore</li><li>Cambodia</li></ul>
<div class="abs f-div" style="left:348px"></div>
<div class="abs f-head" style="left:402px;top:906px">Partners/ Merchants</div>
<ul class="abs f-list" style="left:402px;top:938px"><li>Become a partner</li><li>Education</li><li>Non-Profits</li></ul>
<ul class="abs f-list" style="left:553px;top:938px"><li>Reseller</li><li>Affiliates</li></ul>
<div class="abs f-div" style="left:648px"></div>
<div class="abs f-head" style="left:694px;top:906px">Need Help?</div>
<ul class="abs f-list" style="left:697px;top:938px"><li>Customer Support</li><li>Live Chat Support</li><li>Track a transaction</li></ul>
<div class="abs f-div" style="left:848px"></div>
<div class="abs f-head" style="left:892px;top:906px">Join Our Community</div>
<a class="abs f-link" href="#" style="left:892px;top:934px">Newsletter Sing up</a>
<div class="abs f-fan" style="left:892px;top:963px">Become a fan</div>
<span class="abs social" style="left:892px;background:#4fb3e4"></span>
<span class="abs social" style="left:920px;background:var(--navy)"></span>
<span class="abs social" style="left:948px;background:#d84a3a"></span>
<span class="abs social" style="left:976px;background:#1d3f86"></span>

<div class="abs legal">Press Releases<span>|</span>Privacy Statement<span>|</span>Terms of Use<span>|</span>Jobs<span>|</span>Sitemap<span>|</span>Tell us what you think</div>
<div class="abs copyright">Copyright © 2010 Tarrow Labs Co. Ltd</div>

</body>
</html>
```